Commercial real estate Brokerage logo, letterhead and business card design

Boutique Commercial real Estate Brokerage and development company requires logo, letterhead/stationary and business card design. For reference, competitors include Harlow Brent Tavistock, Pendry & Marlowe, Ridgeway Olcott and Brantham which all have designs which evoke strong corporate image.

The name of the firm is Dunsworth Real Estate. If you look at my competitors web sites you will see their logos. I am looking for something that has a similar flavor - not the same colors or graphics - just how you feel when you see their logo. 
1. www.hbt-realty.example
2. http://www.branthamgroup.example/en-us
3. http://www.pendrymarlowe.example/

```html
<!DOCTYPE html>
<html lang="en">
<head>
<meta charset="utf-8">
<title>Dunsworth Real Estate — Stationery Set</title>
<link rel="stylesheet" href="https://fonts.googleapis.com/css2?family=Arimo:wght@400;700&display=swap">
<style>
  :root {
    --bg: #e9e6e1;
    --paper: #ffffff;
    --ink: #1e1e1e;
    --teal: #5a8a78;
    --orange: #ff6a00;
    --blue: #3399ff;
    --watermark: rgba(90, 138, 120, 0.09);
  }
  * { box-sizing: border-box; margin: 0; padding: 0; }
  html, body { width: 1200px; height: 562px; overflow: hidden; }
  body { background: var(--bg); font-family: "Arimo", Arial, sans-serif; color: var(--ink); position: relative; }

  .sheet, .envelope, .card { position: absolute; background: var(--paper); box-shadow: 0 2px 5px rgba(0,0,0,.18); }

  .brand { position: absolute; display: flex; align-items: center; gap: 5px; color: var(--teal); font-weight: 400; white-space: nowrap; }
  .brand-dot { width: 12px; height: 12px; border-radius: 50%; background: var(--orange); flex: none; }

  .contact-icon { display: inline-block; width: 6px; height: 6px; border-radius: 50%; background: var(--ink); margin-right: 3px; vertical-align: middle; position: relative; top: -1px; }

  /* Letterhead */
  .letterhead { left: 20px; top: 69px; width: 330px; height: 427px; }
  .letterhead .brand { left: 18px; top: 20px; font-size: 9px; }
  .contact-list { position: absolute; right: 10px; top: 8px; border-left: 1px solid var(--ink); padding-left: 4px; font-size: 8.4px; line-height: 10px; list-style: none; white-space: nowrap; }
  .watermark { position: absolute; left: 60px; top: 150px; width: 210px; height: 210px; border-radius: 50%; background: var(--watermark); display: flex; align-items: center; justify-content: center; color: rgba(255,106,0,.16); font-size: 17px; }
  .letterhead .footer-address { position: absolute; left: 0; right: 0; top: 408px; text-align: center; font-size: 8px; }
  .letterhead .footer-band { position: absolute; left: 0; bottom: 0; width: 100%; height: 7px; }

  /* Fax */
  .fax { left: 376px; top: 69px; width: 330px; height: 427px; background: linear-gradient(160deg, #fbfbfb, #e4e4e4); }
  .fax .brand { left: 18px; top: 26px; font-size: 9px; }
  .fax-address { position: absolute; left: 236px; top: 19px; border-left: 1px solid var(--ink); padding-left: 4px; font-size: 8px; line-height: 10px; white-space: nowrap; }
  .fax-title { position: absolute; left: 17px; top: 92px; font-size: 19px; font-weight: 400; }
  .fax-field { position: absolute; height: 11px; border-bottom: 1px solid #555; font-size: 5.6px; line-height: 8px; }
  .fax-checks { position: absolute; left: 17px; top: 209px; display: flex; font-size: 5.6px; white-space: nowrap; }
  .fax-checks span { display: flex; align-items: center; gap: 4px; margin-right: 10px; }
  .fax-checks span::before { content: ""; width: 7px; height: 7px; border: 1px solid #333; background: #fff; }
  .fax-footer { position: absolute; left: 9px; top: 410px; font-size: 8.2px; white-space: nowrap; }

  /* Envelopes */
  .envelope-back { left: 742px; top: 22px; width: 368px; height: 164px; background: linear-gradient(180deg, #fff, #e6e6e6); }
  .envelope-open { left: 734px; top: 117px; width: 370px; height: 165px; background: linear-gradient(180deg, #f4f4f4, #dedede); border: 1px solid #aaa; }
  .envelope-open .brand { left: 50%; top: 42px; transform: translateX(-50%); font-size: 11px; }
  .envelope-front { left: 752px; top: 200px; width: 368px; height: 164px; background: linear-gradient(160deg, #fff, #ececec); border: 1px solid #bbb; }
  .envelope-front .brand { left: 10px; top: 18px; font-size: 8px; }
  .envelope-front .return-address { position: absolute; left: 9px; top: 135px; font-size: 8px; line-height: 11px; white-space: nowrap; }

  /* Business cards */
  .card-front { left: 744px; top: 382px; width: 212px; height: 122px; background: #fdfdf9; }
  .card-front .brand { left: 50%; top: 44px; transform: translateX(-50%); font-size: 8px; }
  .card-person { position: absolute; left: 0; width: 94px; top: 75px; text-align: right; font-size: 5.8px; line-height: 7px; }
  .card-person .name { font-size: 7px; }
  .card-person .gap { margin-top: 4px; }
  .card-contacts { position: absolute; left: 101px; top: 73px; border-left: 1px solid var(--ink); padding-left: 5px; list-style: none; font-size: 5.8px; line-height: 8px; white-space: nowrap; }
  .card-contacts .contact-icon { width: 4px; height: 4px; top: 0; }
  .card-band { position: absolute; left: 0; bottom: 0; width: 100%; height: 5px; }

  .card-back { left: 966px; top: 382px; width: 213px; height: 120px; }
  .card-back .brand { left: 50%; top: 42px; transform: translateX(-50%); font-size: 13px; gap: 7px; }
  .card-back .brand-dot { width: 16px; height: 16px; }
  .card-back .url { position: absolute; left: 0; right: 0; top: 98px; text-align: center; font-size: 7.5px; letter-spacing: .5px; }
</style>
</head>
<body>

  <section class="sheet letterhead">
    <div class="brand"><span class="brand-dot"></span>Dunsworth Real Estate</div>
    <ul class="contact-list">
      <li><span class="contact-icon"></span>123-456-7890</li>
      <li><span class="contact-icon"></span>123-456-7890</li>
      <li><span class="contact-icon"></span>hello@dunsworth.example</li>
      <li><span class="contact-icon"></span>www.dunsworth.example</li>
    </ul>
    <div class="watermark">Dunsworth Real Estate</div>
    <p class="footer-address">Street Name, City Name State Zip code</p>
    <svg class="footer-band" viewBox="0 0 330 7" preserveAspectRatio="none">
      <polygon points="0,0 160,0 152,7 0,7" fill="var(--orange)"/>
      <polygon points="164,0 330,0 330,7 156,7" fill="var(--blue)"/>
    </svg>
  </section>

  <section class="sheet fax">
    <div class="brand"><span class="brand-dot"></span>Dunsworth Real Estate</div>
    <p class="fax-address">Street Name, City Name<br>State, Zip Code</p>
    <h1 class="fax-title">FAX</h1>
    <div class="fax-field" style="left:17px;top:124px;width:170px">To :</div>
    <div class="fax-field" style="left:186px;top:124px;width:114px">From :</div>
    <div class="fax-field" style="left:17px;top:141px;width:170px">Fax :</div>
    <div class="fax-field" style="left:186px;top:141px;width:114px">Pages :</div>
    <div class="fax-field" style="left:17px;top:158px;width:170px">Phone :</div>
    <div class="fax-field" style="left:186px;top:158px;width:114px">Date :</div>
    <div class="fax-field" style="left:17px;top:176px;width:170px">Re :</div>
    <div class="fax-field" style="left:186px;top:176px;width:114px">CC :</div>
    <div class="fax-checks">
      <span>Urgent</span><span>For Review</span><span>Please Comment</span><span>Please Reply</span><span>Please Recycle</span>
    </div>
    <p class="fax-footer">123-456-7890 &nbsp;123-456-7890 &nbsp;hello@dunsworth.example &nbsp;www.dunsworth.example</p>
  </section>

  <section class="envelope envelope-back">
    <svg width="368" height="70" viewBox="0 0 368 70" style="position:absolute;left:0;top:0">
      <path d="M0,0 H368 L360,28 Q358,36 340,40 L200,64 Q184,67 168,64 L28,40 Q10,36 8,28 Z" fill="var(--orange)"/>
    </svg>
  </section>

  <section class="envelope envelope-open">
    <svg width="370" height="92" viewBox="0 0 370 92" style="position:absolute;left:0;top:0">
      <path d="M1,1 Q0,14 14,18 L170,86 Q185,92 200,86 L356,18 Q370,14 369,1" fill="#fafafa" stroke="#888" stroke-width="1"/>
    </svg>
    <div class="brand"><span class="brand-dot"></span>Dunsworth Real Estate</div>
  </section>

  <section class="envelope envelope-front">
    <div class="brand"><span class="brand-dot"></span>Dunsworth Real Estate</div>
    <p class="return-address">Street Name, City Name State Zip Code<br>www.dunsworth.example</p>
  </section>

  <section class="card card-front">
    <div class="brand"><span class="brand-dot"></span>Dunsworth Real Estate</div>
    <div class="card-person">
      <div class="name">Your Name</div>
      <div>Position</div>
      <div class="gap">Street Name, City Name<br>State ZipCode</div>
    </div>
    <ul class="card-contacts">
      <li><span class="contact-icon"></span>123-456-7890</li>
      <li><span class="contact-icon"></span>123-456-7890</li>
      <li><span class="contact-icon"></span>hello@dunsworth.example</li>
      <li><span class="contact-icon"></span>www.dunsworth.example</li>
    </ul>
    <svg class="card-band" viewBox="0 0 212 5" preserveAspectRatio="none">
      <polygon points="0,0 102,0 96,5 0,5" fill="var(--teal)"/>
      <polygon points="104,0 212,0 212,5 98,5" fill="var(--orange)"/>
    </svg>
  </section>

  <section class="card card-back">
    <div class="brand"><span class="brand-dot"></span>Dunsworth Real Estate</div>
    <p class="url">www.dunsworth.example</p>
  </section>

</body>
</html>
```